Stonebrook Aerial Business Card

We are a new company based in Central Queensland, Australia that uses specalised drones (Velkor Sprayhawk K40) to undertake mainly agricultural operations, like spraying weeds, spraying crops, spreading seed etc. I have attached a Plinto proof of a card I was thinking along the lines of - purely a start point. The drone used in the business card MUST be a Velkor Sprayhawk K40.
I am very open to other ideas, especially fonts and layout. I don't have website etc set up yet.
The images are stock and easily interchangeable, I just ask that any background images reflect the local central Queensland area. The photo of the drone is not even complete (propellers cut off) and I need a new stock photo – I’m not sure if this is an issue, or I can pay for an image if need be. PLEASE FIND AN SPRAYHAWK K40 image - 4 sprayers, not 6.
The logo/business name is very draft and looking for further ideas, ideally incorporating drones or agriculture design elements into the design of the business name. The business name needs work on the graphic/design – it is a draft that I have included, the drone propellers (being a different colour) are DRAFT only and intended for changes. PLEASE DO NOT USE THE DRONE PORPELLER I HAVE USED AS A DRAFT. TRY TO FIND SOMETHING ELSE.. The arrow is a shape and not aligned in any way, I would also like ideas on different fonts and additional elements, like air streams, aviation elements, aviation or country western (farming like) themes and fonts etc.
Ideally looking at staying within the blue, green and yellow colours, keeping with an natural, outdoorsy, environmental feel.

Target Market(s)

Farmers, Agriculture, Local Governments, Land Managers

Industry/Entity Type

Agriculture, Drones, Aviation

Contact Information for Business Card

Agricultural Drone (Velkor Sprayhawk K40), Farming, Business Name.

Font styles to use
Sans Serif

Colors
0054AA
0677BA
7BADD7
CADEEF
E8F1F8
0094D4
00A9DD
6FCCEA
C7EBF8
E9F6FB
00AB8E
00BBA5
67D7C9
C6EFE9
E9F9F6
59FF00
82FF00
B8FF75
E3FFCB
F4FFEA

Requirements
Must have
• Velkor Sprayhawk K40 Drone
Should not have
• Tractors

```html
<!DOCTYPE html>
<html lang="en">
<head>
<meta charset="utf-8">
<title>Stonebrook Aerial Business Card</title>
<link rel="stylesheet" href="https://fonts.googleapis.com/css2?family=Montserrat:wght@600;700;800&family=Exo+2:ital,wght@1,800&family=Cinzel:wght@700&display=swap">
<style>
  :root {
    --slate: #4a5a73;
    --olive: #7f8b3a;
    --lime: #a9c23f;
    --paper: #ffffff;
    --backdrop: #ececec;
    --shadow: rgba(0,0,0,0.35);
  }
  * { box-sizing: border-box; margin: 0; padding: 0; }
  html, body { width: 1200px; height: 1200px; overflow: hidden; }
  body { background: var(--backdrop); position: relative; font-family: "Montserrat", sans-serif; }

  .card {
    position: absolute;
    left: 254px;
    width: 692px;
    height: 396px;
    background: var(--paper);
    box-shadow: 6px 8px 10px var(--shadow);
    overflow: hidden;
  }
  .card--front { top: 186px; }
  .card--back { top: 626px; }
  .card__waves { position: absolute; inset: 0; width: 100%; height: 100%; }

  .brand {
    position: absolute;
    left: 0; right: 0;
    top: 104px;
    text-align: center;
    font-family: "Montserrat", sans-serif;
    font-weight: 800;
    color: var(--slate);
    font-size: 43px;
    line-height: 46px;
    letter-spacing: 0.5px;
  }
  .tagline {
    position: absolute;
    left: 0; right: 0;
    top: 208px;
    text-align: center;
    font-family: "Cinzel", serif;
    font-weight: 700;
    font-size: 15px;
    color: #1d1d1d;
    letter-spacing: 1px;
  }

  .person { position: absolute; left: 32px; top: 48px; }
  .person__name {
    font-family: "Exo 2", sans-serif;
    font-style: italic;
    font-weight: 800;
    font-size: 29px;
    line-height: 32px;
    color: var(--olive);
  }
  .person__role {
    font-weight: 700;
    font-size: 18px;
    color: var(--slate);
    margin-top: 2px;
  }

  .contacts {
    position: absolute;
    left: 32px;
    top: 176px;
    list-style: none;
    color: var(--slate);
    font-weight: 600;
    font-size: 17px;
    line-height: 22px;
  }
  .contacts__item { display: flex; align-items: center; gap: 9px; margin-bottom: 7px; }
  .contacts__item--address { align-items: center; }
  .contacts__icon { width: 16px; height: 16px; flex: none; fill: var(--olive); }

  .drone-photo {
    position: absolute;
    left: 346px;
    top: 128px;
    width: 316px;
    height: 112px;
    border-radius: 8px;
    background: radial-gradient(ellipse at 50% 45%, #cfcfcf 0%, #8a8a8a 35%, #e6e6e6 75%, #ffffff 100%);
  }
</style>
</head>
<body>

<section class="card card--front">
  <svg class="card__waves" viewBox="0 0 577 330" preserveAspectRatio="none" aria-hidden="true">
    <path fill="var(--slate)" d="M0,215 C120,222 250,245 340,275 C410,296 470,292 512,276 C470,302 400,306 330,292 C250,268 120,240 0,234 Z"/>
    <path fill="var(--olive)" d="M0,248 C110,250 210,268 310,298 C400,322 500,312 577,262 L577,330 L0,330 Z"/>
    <path fill="var(--lime)" d="M455,318 C515,305 552,283 577,252 L577,288 C545,308 505,318 455,320 Z"/>
  </svg>
  <h1 class="brand">STONEBROOK<br>AERIAL</h1>
  <p class="tagline">Servicing Central Queensland</p>
</section>

<section class="card card--back">
  <svg class="card__waves" viewBox="0 0 577 330" preserveAspectRatio="none" aria-hidden="true">
    <path fill="var(--slate)" d="M0,250 C15,290 90,314 220,318 C120,326 40,316 0,304 Z"/>
    <path fill="var(--olive)" d="M0,282 C120,312 230,262 360,252 C450,246 530,250 577,244 L577,330 L0,330 Z"/>
  </svg>

  <div class="person">
    <h2 class="person__name">LIAM CARTER</h2>
    <p class="person__role">CEO &amp; FOUNDER</p>
  </div>

  <ul class="contacts">
    <li class="contacts__item">
      <svg class="contacts__icon" viewBox="0 0 24 24"><path d="M6.6 10.8a15 15 0 0 0 6.6 6.6l2.2-2.2a1 1 0 0 1 1-.25 11.4 11.4 0 0 0 3.6.57 1 1 0 0 1 1 1V20a1 1 0 0 1-1 1A17 17 0 0 1 3 4a1 1 0 0 1 1-1h3.5a1 1 0 0 1 1 1c0 1.25.2 2.45.57 3.57a1 1 0 0 1-.25 1z"/></svg>
      +61 7 4982 3157
    </li>
    <li class="contacts__item">
      <svg class="contacts__icon" viewBox="0 0 24 24"><circle cx="12" cy="12" r="10" fill="none" stroke="var(--olive)" stroke-width="2.5"/><path d="M2 12h20M12 2c3 3 3 17 0 20M12 2c-3 3-3 17 0 20" fill="none" stroke="var(--olive)" stroke-width="2"/></svg>
      STONEBROOKAERIAL.COM
    </li>
    <li class="contacts__item">
      <svg class="contacts__icon" viewBox="0 0 24 24"><path d="M2 5h20v14H2z"/><path d="M2 5l10 8 10-8" fill="none" stroke="#fff" stroke-width="2"/></svg>
      LIAM@STONEBROOKAERIAL.COM
    </li>
    <li class="contacts__item contacts__item--address">
      <svg class="contacts__icon" viewBox="0 0 24 24"><path d="M12 2a7 7 0 0 0-7 7c0 5 7 13 7 13s7-8 7-13a7 7 0 0 0-7-7zm0 9.5A2.5 2.5 0 1 1 12 6.5a2.5 2.5 0 0 1 0 5z"/></svg>
      <span>18 QUARRY LANE,<br>SUITE 4, EMERALD,<br>QLD 4720</span>
    </li>
  </ul>

  <div class="drone-photo" role="img" aria-label="Photo of a Velkor Sprayhawk K40 agricultural spray drone in flight"></div>
</section>

</body>
</html>
```